Online Course Page

We are building a video based online course page. This project is for only the actual page that the student will watch the videos at. They will watch one vide at a time. Once one video lesson is completed then they can move to the next video lesson. The page will need to show the video player. (Main feature.) The list of lessons in the course. Instructor information. Profile picture and bio of the instructor. A Live chat button that will initiate a chat in real-time with the instructor.

The winning designer will also be asked to to design the dashboard area and other aspects of the user interface as an additional project.

Target Market(s)

Adults

Number of Pages Required

1 page

Colors
9bcb3c

Requirements
Must have
• Our logo is attached. Green and grey are our colors. Should feel modern, clean and be simple to navigate. The site will be responsive so the layout should work well on mobile devices.

```html
<!DOCTYPE html>
<html lang="en">
<head>
<meta charset="utf-8">
<title>CSS Grid Layout – LearnHarbor</title>
<link href="https://fonts.googleapis.com/css2?family=Roboto:wght@300;400;500;700&display=swap" rel="stylesheet">
<style>
:root{
  --green:#9bcb3c;
  --page:#ececec;
  --card:#f7f7f7;
  --white:#ffffff;
  --ink:#3f4247;
  --text:#555a5f;
  --line:#dddddd;
  --footer:#555555;
  --footer-text:#d6d6d6;
  --video:#0a1e52;
  --video-deep:#041035;
}
*{box-sizing:border-box;margin:0;padding:0}
html,body{width:838px;height:1200px;overflow:hidden}
body{position:relative;background:var(--page);font-family:"Roboto",sans-serif;color:var(--ink)}

.site-header{position:absolute;left:0;top:0;width:838px;height:52px;background:var(--white)}
.brand{position:absolute;left:52px;top:16px;display:flex;align-items:center;gap:6px;font-size:15px;font-weight:700;color:var(--ink)}
.brand-dot{width:14px;height:14px;border-radius:50%;background:var(--green)}
.search{position:absolute;left:178px;top:12px;width:231px;height:25px;border:1px solid #e0e0e0;background:#f7f7f7;border-radius:2px;font-size:10px;color:#a3a6a9;padding:7px 12px;font-weight:300}
.search svg{position:absolute;right:12px;top:6px}
.nav{position:absolute;top:19px;font-size:10.5px;color:var(--text);display:flex;align-items:center;gap:4px}
.nav.courses{left:429px}
.nav.categories{left:496px}
.account{position:absolute;left:748px;top:13px;display:flex;align-items:center;gap:4px}

.page-title{position:absolute;left:52px;top:73px;font-size:20.5px;font-weight:500;color:var(--ink)}

.player-card{position:absolute;left:51px;top:122px;width:484px;height:311px;background:var(--card)}
.video{position:absolute;left:0;top:0;width:484px;height:272px;background:linear-gradient(135deg,var(--video) 0%,#0d2a78 45%,var(--video-deep) 100%)}
.controls{position:absolute;left:0;top:242px;width:484px;height:30px;background:linear-gradient(transparent,rgba(0,0,0,.55))}
.progress{position:absolute;left:13px;top:248px;width:458px;height:3px;background:#666}
.progress-fill{width:68px;height:3px;background:var(--green)}
.play{position:absolute;left:26px;top:256px}
.time{position:absolute;left:60px;top:256px;font-size:10px;color:#fff}
.fullscreen{position:absolute;left:445px;top:255px}
.next-lesson{position:absolute;right:12px;top:287px;font-size:10px;font-weight:500;color:var(--green);display:flex;align-items:center;gap:4px}

.instructor{position:absolute;left:554px;top:122px;width:232px;height:310px;background:var(--card);padding:12px 11px}
.instructor h2{font-size:12px;font-weight:500;color:var(--ink)}
.portrait{position:absolute;left:11px;top:39px;width:80px;height:80px;border-radius:50%;background:radial-gradient(circle at 50% 40%,#c99b7e 0%,#6e5446 55%,#3d4c5c 100%)}
.instructor-name{position:absolute;left:111px;top:50px;font-size:10.5px;color:var(--text);font-weight:300}
.live-chat{position:absolute;left:111px;top:75px;width:93px;height:25px;background:var(--green);color:#fff;font-size:10px;font-weight:500;display:flex;align-items:center;justify-content:center;gap:6px;border-radius:1px}
.bio{position:absolute;left:11px;top:143px;width:206px;font-size:10px;line-height:13px;color:var(--text);font-weight:300}
.show-more{position:absolute;left:11px;top:260px;font-size:10px;font-weight:500;color:var(--ink);display:flex;align-items:center;gap:4px}

.course{position:absolute;left:52px;top:459px;width:484px;height:536px;background:var(--card);padding:20px 14px 0 12px}
.course h2{font-size:14.5px;font-weight:500;color:var(--ink)}
.about p{margin-top:6px;font-size:9.8px;line-height:17px;color:var(--text);font-weight:300}
.section{margin-top:28px}
.section + .section{margin-top:26px}
.section h3{font-size:14.5px;font-weight:400;color:var(--ink);margin-bottom:17px}
.lessons{list-style:none;border-top:1px solid var(--line)}
.lesson{height:32.3px;border-bottom:1px solid var(--line);display:flex;align-items:center;font-size:10px;font-weight:500;color:var(--ink)}
.lesson-title{flex:1}
.lesson-time{width:46px;font-weight:300;color:var(--text)}
.lesson .play-icon{width:18px;height:18px}

.site-footer{position:absolute;left:0;top:1046px;width:838px;height:154px;background:var(--footer);color:var(--footer-text)}
.footer-col{position:absolute;top:38px}
.footer-col h4{font-size:11.5px;font-weight:500;color:#fff;margin-bottom:8px}
.footer-col a{display:block;font-size:10px;font-weight:300;color:var(--footer-text);text-decoration:none;margin-bottom:8px}
.footer-col.brand-col{left:53px}
.footer-col.support{left:241px}
.footer-col.join{left:557px}
.social{display:flex;gap:30px;margin-top:6px}
.social span{width:14px;height:14px;border-radius:50%;background:var(--footer-text)}
.footer-rule{position:absolute;left:0;top:129px;width:838px;height:1px;background:#777}
.copyright{position:absolute;left:52px;top:138px;font-size:9.5px;font-weight:300;color:var(--footer-text)}
</style>
</head>
<body>

<header class="site-header">
  <div class="brand"><span class="brand-dot"></span>LearnHarbor</div>
  <div class="search">Search for courses
    <svg width="12" height="12" viewBox="0 0 12 12" fill="none" stroke="#b5b8bb" stroke-width="1.2"><circle cx="5" cy="5" r="3.8"/><path d="M8 8l3 3"/></svg>
  </div>
  <div class="nav courses">Courses <svg width="8" height="5" viewBox="0 0 8 5"><path d="M1 1l3 3 3-3" fill="none" stroke="#555" stroke-width="1"/></svg></div>
  <div class="nav categories">Catergories <svg width="8" height="5" viewBox="0 0 8 5"><path d="M1 1l3 3 3-3" fill="none" stroke="#555" stroke-width="1"/></svg></div>
  <div class="account">
    <svg width="26" height="26" viewBox="0 0 26 26" fill="none" stroke="#666" stroke-width="1"><circle cx="13" cy="13" r="12.3"/><circle cx="13" cy="10" r="4"/><path d="M5.5 21c1.8-3.5 4.5-5 7.5-5s5.7 1.5 7.5 5"/></svg>
    <svg width="8" height="5" viewBox="0 0 8 5"><path d="M1 1l3 3 3-3" fill="none" stroke="#555" stroke-width="1"/></svg>
  </div>
</header>

<h1 class="page-title">CSS Grid Layout</h1>

<section class="player-card">
  <div class="video" role="img" aria-label="Lesson video frame showing CSS code on a dark blue screen"></div>
  <div class="controls"></div>
  <div class="progress"><div class="progress-fill"></div></div>
  <svg class="play" width="9" height="11" viewBox="0 0 9 11"><path d="M0 0l9 5.5L0 11z" fill="#fff"/></svg>
  <span class="time">1:34/4:44</span>
  <svg class="fullscreen" width="13" height="13" viewBox="0 0 13 13" fill="none" stroke="#fff" stroke-width="1.2"><path d="M1 4V1h3M9 1h3v3M12 9v3H9M4 12H1V9"/><rect x="3.5" y="3.5" width="6" height="6"/></svg>
  <div class="next-lesson">Next Lesson <svg width="5" height="8" viewBox="0 0 5 8"><path d="M1 1l3 3-3 3" fill="none" stroke="#9bcb3c" stroke-width="1.2"/></svg></div>
</section>

<aside class="instructor">
  <h2>Instructor</h2>
  <div class="portrait" role="img" aria-label="Instructor profile photo"></div>
  <div class="instructor-name">John Somebody</div>
  <div class="live-chat">
    <svg width="15" height="12" viewBox="0 0 15 12" fill="none" stroke="#fff" stroke-width="1"><path d="M1.5 1h12v7.5H6L3 11V8.5H1.5z"/></svg>
    Live Chat
  </div>
  <p class="bio">Lorem ipsum dolor sit amet, consectetur adipiscing elit. In aliquam nisi vel elit consectetur vehicula. In enim tellus, efficitur at tristique vehicula, gravida vitae sem. Morbi eu pulvinar lectus. Curabitur quam odio, vehicula varius luctus ut, mattis nec purus. Nam elementum nibh vel nisl fermentum rhoncus.</p>
  <div class="show-more">Show More <svg width="5" height="8" viewBox="0 0 5 8"><path d="M1 1l3 3-3 3" fill="none" stroke="#3f4247" stroke-width="1.2"/></svg></div>
</aside>

<main class="course">
  <div class="about">
    <h2>About the course.</h2>
    <p>Lorem ipsum dolor sit amet, consectetur adipiscing elit. In aliquam nisi vel elit consectetur vehicula. In enim tellus, efficitur at tristique vehicula, gravida vitae sem. Morbi eu pulvinar lectus. Curabitur quam odio, vehicula varius luctus ut, mattis nec purus.</p>
  </div>

  <div class="section">
    <h3>Introducing Grid Layout</h3>
    <ul class="lessons">
      <li class="lesson"><span class="lesson-title">Understanding Grid</span><span class="lesson-time">3:21</span><svg class="play-icon" viewBox="0 0 18 18" fill="none" stroke="#aaa"><circle cx="9" cy="9" r="8.3"/><path d="M7 5.5l5 3.5-5 3.5z"/></svg></li>
      <li class="lesson"><span class="lesson-title">Grid Concepts and Terminology</span><span class="lesson-time">2.:31</span><svg class="play-icon" viewBox="0 0 18 18" fill="none" stroke="#aaa"><circle cx="9" cy="9" r="8.3"/><path d="M7 5.5l5 3.5-5 3.5z"/></svg></li>
      <li class="lesson"><span class="lesson-title">Defining a Gid</span><span class="lesson-time">4:55</span><svg class="play-icon" viewBox="0 0 18 18" fill="none" stroke="#aaa"><circle cx="9" cy="9" r="8.3"/><path d="M7 5.5l5 3.5-5 3.5z"/></svg></li>
      <li class="lesson"><span class="lesson-title">Setting Grid Rows</span><span class="lesson-time">5:23</span><svg class="play-icon" viewBox="0 0 18 18" fill="none" stroke="#aaa"><circle cx="9" cy="9" r="8.3"/><path d="M7 5.5l5 3.5-5 3.5z"/></svg></li>
      <li class="lesson"><span class="lesson-title">Add Gutters Between Rows and Columns</span><span class="lesson-time">4:33</span><svg class="play-icon" viewBox="0 0 18 18" fill="none" stroke="#aaa"><circle cx="9" cy="9" r="8.3"/><path d="M7 5.5l5 3.5-5 3.5z"/></svg></li>
    </ul>
  </div>

  <div class="section">
    <h3>Flexible Sized Grids</h3>
    <ul class="lessons">
      <li class="lesson"><span class="lesson-title">Flexible Tracks</span><span class="lesson-time">3:21</span><svg class="play-icon" viewBox="0 0 18 18" fill="none" stroke="#aaa"><circle cx="9" cy="9" r="8.3"/><path d="M7 5.5l5 3.5-5 3.5z"/></svg></li>
      <li class="lesson"><span class="lesson-title">Set Tracks with repeat() Notation</span><span class="lesson-time">2.:31</span><svg class="play-icon" viewBox="0 0 18 18" fill="none" stroke="#aaa"><circle cx="9" cy="9" r="8.3"/><path d="M7 5.5l5 3.5-5 3.5z"/></svg></li>
      <li class="lesson"><span class="lesson-title">Auto-generate Flexible Columns</span><span class="lesson-time">4:55</span><svg class="play-icon" viewBox="0 0 18 18" fill="none" stroke="#aaa"><circle cx="9" cy="9" r="8.3"/><path d="M7 5.5l5 3.5-5 3.5z"/></svg></li>
    </ul>
  </div>
</main>

<footer class="site-footer">
  <div class="footer-col brand-col">
    <h4>Learn Harbor</h4>
    <a href="#">About Learn Harbor</a>
  </div>
  <div class="footer-col support">
    <h4>Support</h4>
    <a href="#">Contact US</a>
    <a href="#">FAQ</a>
    <a href="#">Help Center</a>
  </div>
  <div class="footer-col join">
    <h4>Join Us</h4>
    <div class="social"><span></span><span></span></div>
  </div>
  <div class="footer-rule"></div>
  <div class="copyright">© Copyright 2018</div>
</footer>

</body>
</html>
```